Brierley Dunmore Lawyers needs a web design

We need a web design for our conveyancing and commercial law firm based in Sydney Australia. We want to depersonalise the current website: http://www.brierleydunmore.example/ and give it a classic modern feel to it. It should be a simple design (possibly one page) and communicate trust, professionalism and experience.

Content should include:

Brierley Dunmore is a boutique Sydney based legal practice specialising in business and property law.

We pride ourselves on our proactive, receptive and dynamic approach to client service. Our business survives on referrals from satisfied clients and professionals who respect the way we do business.

Practice areas

Business law

We act on the sale and purchase of businesses. We assist clients with structuring their businesses, drafting shareholder agreements and buy-sell arrangements. We have acted on a multitude of other commercial matters including franchising, distribution, marketing and business services (with a particular focus in the advertising sector).

Property law

We act for developers, commercial property investors, landlords and tenants. We also handle residential conveyancing and deal with strata and company title matters.

Private Client

We draft wills and codicils on behalf of clients and can also assist with applications for probate should the need arise.

Contact Us

Brierley Dunmore
Level 29, Wexcombe Tower
7 Marlowe Square
Sydney, NSW 2000

t: +61 (0)2 9471 6203
f: +61 (0)2 8526 4079
e: enquiries@brierleydunmore.example

Target Market(s)

Individuals and business who need legal advice in the area of property and commercial law

Industry/Entity Type

Legal

Number of Pages Required

1 page

Font styles to use
Sans Serif

Requirements
Must have
• Clear and concise content.
Nice to have
• Some images to break up the content.
Should not have
• Any offensive images tones or connotations.

```html
<!DOCTYPE html>
<html lang="en">
<head>
<meta charset="utf-8">
<title>Brierley Dunmore Lawyers</title>
<link rel="stylesheet" href="https://fonts.googleapis.com/css2?family=Questrial&family=Open+Sans:wght@400;600&family=Signika:wght@600&display=swap">
<style>
:root{
  --black:#000;
  --navy:#0e2d80;
  --blue:#1d3a8a;
  --ink:#555;
  --muted:#777;
  --white:#fff;
  --contact:#1c1c1c;
}
*{box-sizing:border-box;margin:0;padding:0}
html,body{width:704px;height:1200px;overflow:hidden;background:var(--white)}
body{position:relative;font-family:"Open Sans",sans-serif}
.site-header{position:absolute;left:0;top:0;width:704px;height:72px;background:var(--black)}
.brand{position:absolute;left:28px;top:22px;color:#bbb;font-family:"Questrial",sans-serif;font-size:16px;line-height:17px}
.brand small{display:block;font-size:8px;line-height:10px;text-align:right}
.main-nav{position:absolute;top:28px;left:0;font-size:6.6px;color:var(--white);text-transform:uppercase}
.main-nav span{position:absolute;white-space:nowrap}
.main-nav .active{color:#2f56c8}
.social{position:absolute;top:23px;width:15px;height:15px;border:1px solid #ccc}
.hero{position:absolute;left:0;top:72px;width:704px;height:369px;background:linear-gradient(100deg,#6c7480 0%,#8b929c 35%,#5e6570 65%,#3d434c 100%)}
.hero-rule{position:absolute;left:117px;width:461px;height:1px;background:rgba(255,255,255,.55)}
.hero h1{position:absolute;left:0;width:704px;top:125px;text-align:center;font-family:"Questrial",sans-serif;font-weight:400;font-size:21px;color:var(--white)}
.hero p{position:absolute;left:118px;width:468px;top:168px;text-align:center;font-size:8.6px;line-height:13px;color:#eee}
.btn{position:absolute;background:var(--navy);color:var(--white);font-size:6.6px;text-align:center;text-transform:uppercase}
.dots{position:absolute;top:274px;left:333px;display:flex;gap:8px}
.dots i{width:7px;height:7px;border:1px solid #eee;border-radius:50%}
.dots i.on{background:#fff}
.welcome{position:absolute;left:0;top:441px;width:704px;height:186px;background:linear-gradient(#fff,#eee)}
.section-title{position:absolute;left:0;width:704px;text-align:center;font-family:"Questrial",sans-serif;font-size:17px;color:#666;font-weight:400}
.section-title em{font-style:normal;color:var(--navy)}
.welcome p{position:absolute;left:80px;width:544px;text-align:center;font-size:6.8px;line-height:13px;color:var(--muted)}
.tile{position:absolute;overflow:hidden}
.tile-business{left:28px;top:711px;width:398px;height:299px;background:linear-gradient(135deg,#2a4a96,#1a3680 60%,#16306f)}
.tile-property{left:428px;top:711px;width:248px;height:148px;background:linear-gradient(#d8a88a,#e9c9b0 55%,#f2efe9)}
.tile-private{left:428px;top:862px;width:248px;height:148px;background:linear-gradient(120deg,#5a5a5a,#c8b5a3 50%,#e8e6e8)}
.tile-label{position:absolute;left:42px;width:176px;height:35px;background:rgba(58,70,130,.78);color:var(--white);font-family:"Signika",sans-serif;font-weight:600;font-size:17px;line-height:35px;text-align:center;letter-spacing:.3px}
.tile-business h3{position:absolute;left:0;width:398px;top:106px;text-align:center;font-family:"Signika",sans-serif;font-weight:600;font-size:17px;color:var(--white)}
.tile-business p{position:absolute;left:42px;width:314px;top:138px;text-align:center;font-size:6.8px;line-height:11px;color:var(--white)}
.tile-business svg{position:absolute;left:193px;top:195px}
.contact{position:absolute;left:0;top:1037px;width:704px;height:108px;background:var(--contact)}
.contact-item{position:absolute;display:flex;align-items:center;gap:11px;color:var(--white);font-size:11.8px;white-space:nowrap}
.contact-icon{width:23px;height:23px;border:1px solid #888;display:flex;align-items:center;justify-content:center}
.site-footer{position:absolute;left:0;top:1145px;width:704px;height:55px;background:var(--black);color:#ddd;font-size:6.6px;text-align:center;line-height:55px}
</style>
</head>
<body>
<header class="site-header">
  <div class="brand">Brierley Dunmore<small>Lawyers</small></div>
  <nav class="main-nav">
    <span class="active" style="left:272px">Home</span>
    <span style="left:320px">Our People</span>
    <span style="left:388px">Practice Areas</span>
    <span style="left:469px">Testimonials</span>
    <span style="left:544px">Contact Us</span>
  </nav>
  <span class="social" style="left:618px"></span>
  <span class="social" style="left:640px"></span>
  <span class="social" style="left:661px"></span>
</header>

<section class="hero" role="img" aria-label="Photo of a smiling lawyer in a grey suit seated in a bright office">
  <div class="hero-rule" style="top:114px"></div>
  <h1>LOREM IPSUM DOLOR SIT AMET, CONSECTETUR</h1>
  <div class="hero-rule" style="top:158px"></div>
  <p>Lorem ipsum dolor sit amet, consectetur adipiscing elit, sed do eiusmod tempor incididunt ut labore et dolo-reLorem ipsum dolor sit amet, consectetur adipiscing elit, sed do eiusmod tempor incididunt</p>
  <div class="btn" style="left:313px;top:217px;width:78px;height:25px;line-height:25px">Read More</div>
  <div class="dots"><i></i><i class="on"></i><i></i></div>
</section>

<section class="welcome">
  <h2 class="section-title" style="top:39px">WELCOME TO <em>BRIERLEYDUNMORE LAWYER</em></h2>
  <p style="top:74px">Brierley Dunmore is a boutique Sydney based legal practice specialising in business and property law.</p>
  <p style="top:95px">We pride ourselves on our proactive, receptive and dynamic approach to client service. Our business survives on referrals from satisfied clients and professionals who respect the way we do business.</p>
  <div class="btn" style="left:324px;top:136px;width:67px;height:20px;line-height:20px">Read More</div>
</section>

<h2 class="section-title" style="top:662px">OUR <em>SERVICES</em></h2>

<article class="tile tile-business" role="img" aria-label="Blue-tinted photo of a business meeting signing documents">
  <h3>BUSINESS LAW</h3>
  <p>We act on the sale and purchase of businesses. We assist clients with structuring their businesses, drafting shareholder agreements and buy-sell arrangements. We have acted on a multitude of other commercial matters including franchising, distribution, marketing and business services (with a particular focus in the advertising sector).</p>
  <svg width="11" height="11" viewBox="0 0 12 12"><circle cx="6" cy="6" r="6" fill="#fff"/><path d="M3 6h5M6 3.5 8.5 6 6 8.5" stroke="#1a3680" stroke-width="1.5" fill="none"/></svg>
</article>
<article class="tile tile-property" role="img" aria-label="Photo of cupped hands sheltering a model house">
  <div class="tile-label" style="top:77px">PROPERTY LAW</div>
</article>
<article class="tile tile-private" role="img" aria-label="Photo of a couple meeting with an adviser">
  <div class="tile-label" style="top:80px">PRIVATE CLIENT</div>
</article>

<section class="contact" role="img" aria-label="Dark street map background with contact details">
  <div class="contact-item" style="left:55px;top:30px"><span class="contact-icon"><svg width="12" height="12" viewBox="0 0 12 12"><path d="M2 1h2.5l1 3-1.5 1a6 6 0 0 0 3 3l1-1.5 3 1V11A9 9 0 0 1 1 2z" fill="#fff"/></svg></span>+61 (0)2 9471 6203</div>
  <div class="contact-item" style="left:248px;top:30px"><span class="contact-icon"><svg width="12" height="12" viewBox="0 0 12 12"><rect x="1.5" y="4" width="9" height="7" fill="#fff"/><rect x="3.5" y="1" width="5" height="4" fill="none" stroke="#fff"/></svg></span>+61 (0)2 8526 4079</div>
  <div class="contact-item" style="left:451px;top:30px"><span class="contact-icon"><svg width="12" height="10" viewBox="0 0 12 10"><rect x=".5" y=".5" width="11" height="9" fill="none" stroke="#fff"/><path d="M.5 .5 6 5l5.5-4.5" fill="none" stroke="#fff"/></svg></span>enquiries@brierleydunmore.example</div>
  <div class="contact-item" style="left:55px;top:62px"><span class="contact-icon"><svg width="9" height="12" viewBox="0 0 9 12"><path d="M4.5 12 1 6a4 4 0 1 1 7 0z" fill="#fff"/><circle cx="4.5" cy="4.2" r="1.4" fill="#1c1c1c"/></svg></span>Brierley Dunmore,&nbsp; Level 29, Wexcombe Tower,&nbsp;&nbsp; 7 Marlowe Square,&nbsp; Sydney, NSW 2000</div>
</section>

<footer class="site-footer">All Right Reserved. Copyright ©2015 BrierleyDunmore</footer>
</body>
</html>
```